Business Card - Corporate Services
Professional
TEMESGEN K OLUWADE
Founder & CEO
7218 42nd ave nw Seattle, WA 98142
TKOluwade@mailbrook.net
RNB-Openroadsahead.net
Along with the information on the front side, this text should be present. "We provide loan services you can depend"
I would like to have the company logo exclusively on the back.
pelvo731 pelvo731
Ok, thank you everyone, no more submissions are needed. We appreciate for all your participation. Thank you.
Hi, if you can find a way to incorporate, "We provide loan services you can depend." Text on the front of the card without the quotation marks. Also, please use the phone number only once.

```html
<!DOCTYPE html>
<html lang="en">
<head>
<meta charset="utf-8">
<title>Business Card – RNB Lending Group</title>
<link rel="stylesheet" href="https://fonts.googleapis.com/css2?family=Open+Sans:wght@400;600&display=swap">
<style>
  :root {
    --page-bg: #e9eaec;
    --card-bg: #ffffff;
    --ink: #3a3d42;
    --navy: #1d3c57;
    --band-dark: #1b4a6b;
    --band-light: #4a86ad;
    --icon-blue: #2f7fb8;
    --rule: #2a2d31;
  }
  * { margin: 0; padding: 0; box-sizing: border-box; }
  html, body {
    width: 1200px; height: 816px; overflow: hidden;
    background: var(--page-bg);
    font-family: "Open Sans", Arial, sans-serif;
    color: var(--ink);
  }
  .card {
    position: absolute; left: 75px; top: 108px;
    width: 1050px; height: 600px;
    background: var(--card-bg);
    border-radius: 34px;
    overflow: hidden;
    box-shadow: 0 12px 30px rgba(0,0,0,.18);
  }
  .brand-block {
    position: absolute; right: 110px; top: 138px;
    display: flex; flex-direction: column; align-items: flex-end;
  }
  .brand {
    display: flex; align-items: center; gap: 14px;
  }
  .brand-mark { width: 24px; height: 24px; background: var(--navy); }
  .brand-name {
    font-size: 36px; font-weight: 400; color: var(--navy);
    letter-spacing: .5px; line-height: 1.2;
  }
  .tagline {
    margin-top: 8px;
    font-size: 14px; font-weight: 400; color: var(--ink);
    letter-spacing: 1.6px; text-transform: uppercase;
  }
  .divider {
    position: absolute; left: 480px; right: 0; top: 246px;
    height: 2px; background: var(--rule);
  }
  .name-band {
    position: absolute; left: 0; top: 300px;
    width: 370px; height: 92px;
    border-radius: 0 46px 46px 0;
    background: linear-gradient(90deg, var(--band-dark), var(--band-light));
    color: #fff; text-align: right;
    padding: 14px 44px 0 0;
  }
  .person-name { font-size: 26px; font-weight: 600; white-space: nowrap; }
  .person-title { font-size: 16px; font-weight: 600; letter-spacing: 1.5px; text-transform: uppercase; margin-top: 2px; }
  .contact-list {
    position: absolute; left: 58px; top: 430px;
    list-style: none;
  }
  .contact-list li {
    display: flex; align-items: center; gap: 16px;
    font-size: 19px; height: 38px;
  }
  .contact-list svg, .address svg { width: 20px; height: 20px; fill: var(--icon-blue); flex: none; }
  .address {
    position: absolute; right: 110px; top: 312px;
    display: flex; gap: 14px; font-size: 20px; line-height: 1.35;
    text-align: right;
  }
  .address svg { margin-top: 4px; }
</style>
</head>
<body>
  <article class="card">
    <div class="brand-block">
      <div class="brand">
        <span class="brand-mark"></span>
        <span class="brand-name">RNB Lending Group, Inc</span>
      </div>
      <p class="tagline">We provide loan services you can depend.</p>
    </div>
    <div class="divider"></div>

    <div class="name-band">
      <p class="person-name">Temesgen K Oluwade</p>
      <p class="person-title">Founder &amp; CEO</p>
    </div>

    <div class="address">
      <svg viewBox="0 0 20 20"><path d="M10 2 1 10h3v8h4.5v-5h3v5H16v-8h3z"/></svg>
      <p>7218 42nd ave nw,<br>Seattle, USA</p>
    </div>

    <ul class="contact-list">
      <li>
        <svg viewBox="0 0 20 20"><path d="M5 2l3 4-2 2c1 2.5 3.5 5 6 6l2-2 4 3-2 3C9 18 2 11 2 4z"/></svg>
        +1 (0206) 55-418-07
      </li>
      <li>
        <svg viewBox="0 0 20 20"><path d="M2 4h16v12H2z" /><path d="M2 4l8 7 8-7" fill="none" stroke="#fff" stroke-width="1.6"/></svg>
        TKOluwade@mailbrook.net
      </li>
      <li>
        <svg viewBox="0 0 20 20"><circle cx="10" cy="10" r="8"/><path d="M2 10h16M10 2c-3 3-3 13 0 16M10 2c3 3 3 13 0 16" fill="none" stroke="#fff" stroke-width="1.3"/></svg>
        RNB-Openroadsahead.net
      </li>
    </ul>
  </article>
</body>
</html>
```